frozen samosa packaging

i require a packaging design to comply with British standard regulations for packaging, it has to be eye catching, modern,, minimalistic, professional and with a hint of traditionality, for a premium quality product (so nothing cartoony).
the front of packaging should contain the name of the company Qalor foods and product name also 100% halal and keep frozen anywhere on the packaging.
the packaging to used will be plastic transparent material with dimensions of length 28cm and width 24cm (image attached) also I have attached a packaging design which I really like.
please bare in mind the packaging design should not look out place in a supermarket.

```html
<!DOCTYPE html>
<html lang="en">
<head>
<meta charset="utf-8">
<title>Qalor Foods – Frozen Samosa Pack</title>
<link rel="stylesheet" href="https://fonts.googleapis.com/css2?family=Noto+Serif:wght@500&display=swap">
<style>
  :root {
    --stage: #e4e8ee;
    --maroon-deep: #5e0006;
    --maroon: #8a0710;
    --crimson: #b0101a;
    --crimson-light: #c7232b;
    --band-dark: #2a0a08;
    --gold: #e2b25a;
    --gold-deep: #a8701f;
    --ivory: #fbf4ec;
    --badge-yellow: #ffe600;
    --badge-ring: #27b7e8;
    --badge-text: #d4141c;
    --pastry-light: #f4c98a;
    --pastry-dark: #c97a35;
  }
  html, body {
    margin: 0;
    padding: 0;
    width: 1200px;
    height: 960px;
    overflow: hidden;
    background: var(--stage);
  }
  .stage {
    position: relative;
    width: 1200px;
    height: 960px;
  }
  .pack {
    position: absolute;
    left: 325px;
    top: 130px;
    width: 553px;
    height: 700px;
  }
  .brand-name {
    font-family: "Noto Serif", serif;
    font-weight: 500;
    font-size: 40px;
    fill: var(--ivory);
    text-anchor: middle;
  }
  .badge-text {
    font-family: "Noto Serif", serif;
    font-weight: 500;
    fill: var(--badge-text);
    text-anchor: middle;
  }
  .badge-text--halal { font-size: 20px; }
  .badge-text--frozen { font-size: 14px; }
</style>
</head>
<body>
<main class="stage">
  <svg class="pack" viewBox="0 0 553 700" xmlns="http://www.w3.org/2000/svg">
    <defs>
      <pattern id="teeth-top" x="0" y="0" width="10" height="8" patternUnits="userSpaceOnUse">
        <polygon points="0,8 5,0 10,8" fill="var(--maroon)"/>
      </pattern>
      <pattern id="teeth-bottom" x="0" y="692" width="10" height="8" patternUnits="userSpaceOnUse">
        <polygon points="0,0 5,8 10,0" fill="var(--maroon-deep)"/>
      </pattern>
      <radialGradient id="panel-glow" cx="0.45" cy="0.45" r="0.7">
        <stop offset="0" stop-color="var(--crimson-light)"/>
        <stop offset="0.6" stop-color="var(--maroon)"/>
        <stop offset="1" stop-color="var(--maroon-deep)"/>
      </radialGradient>
      <linearGradient id="gold-line" x1="0" x2="1">
        <stop offset="0" stop-color="var(--gold-deep)"/>
        <stop offset="0.5" stop-color="var(--gold)"/>
        <stop offset="1" stop-color="var(--gold-deep)"/>
      </linearGradient>
      <radialGradient id="pastry" cx="0.5" cy="0.45" r="0.6">
        <stop offset="0" stop-color="var(--pastry-light)"/>
        <stop offset="1" stop-color="var(--pastry-dark)" stop-opacity="0"/>
      </radialGradient>
    </defs>

    <!-- crimped edges -->
    <rect class="seal-teeth" x="0" y="0" width="553" height="8" fill="url(#teeth-top)"/>
    <rect class="seal-teeth" x="0" y="692" width="553" height="8" fill="url(#teeth-bottom)"/>

    <!-- pack body -->
    <rect class="pack-body" x="0" y="7.5" width="553" height="685" fill="url(#panel-glow)"/>

    <!-- seal stripes -->
    <g class="seal-stripes" stroke="var(--maroon-deep)" stroke-width="2">
      <line x1="0" y1="20" x2="553" y2="20"/>
      <line x1="0" y1="32" x2="553" y2="32"/>
      <line x1="0" y1="44" x2="553" y2="44"/>
      <line x1="0" y1="56" x2="553" y2="56"/>
      <line x1="0" y1="68" x2="553" y2="68"/>
      <line x1="0" y1="640" x2="553" y2="640"/>
      <line x1="0" y1="652" x2="553" y2="652"/>
      <line x1="0" y1="664" x2="553" y2="664"/>
      <line x1="0" y1="676" x2="553" y2="676"/>
    </g>

    <!-- top swoosh -->
    <path class="swoosh-top" d="M0 90 H553 V108 C420 70 200 100 0 160 Z" fill="var(--maroon-deep)"/>
    <path class="swoosh-top-dark" d="M0 140 C200 88 400 68 553 98 V112 C400 88 200 112 0 158 Z" fill="var(--band-dark)"/>
    <path class="swoosh-top-gold" d="M0 150 C200 100 400 82 553 112" fill="none" stroke="url(#gold-line)" stroke-width="3"/>
    <path class="swoosh-top-red" d="M0 128 C200 78 400 60 553 88" fill="none" stroke="var(--crimson)" stroke-width="6"/>

    <!-- bottom swoosh -->
    <path class="swoosh-bottom" d="M0 500 C150 560 400 570 553 530 V632 H0 Z" fill="var(--maroon-deep)"/>
    <path class="swoosh-bottom-dark" d="M0 520 C150 580 400 592 553 552 V572 C400 610 150 600 0 545 Z" fill="var(--band-dark)"/>
    <path class="swoosh-bottom-gold" d="M0 512 C150 570 400 582 553 542" fill="none" stroke="url(#gold-line)" stroke-width="3"/>
    <path class="swoosh-bottom-red" d="M0 556 C150 612 400 622 553 584" fill="none" stroke="var(--crimson)" stroke-width="6"/>

    <!-- brand name -->
    <text class="brand-name" x="312" y="232">Qalor Foods</text>

    <!-- product photo area -->
    <g role="img" aria-label="Photograph of two golden fried samosas">
      <ellipse cx="310" cy="418" rx="165" ry="112" fill="url(#pastry)"/>
    </g>

    <!-- 100% halal badge -->
    <g class="badge badge--halal" transform="translate(126 253)">
      <g fill="var(--badge-yellow)">
        <rect x="-38" y="-38" width="76" height="76"/>
        <rect x="-38" y="-38" width="76" height="76" transform="rotate(15)"/>
        <rect x="-38" y="-38" width="76" height="76" transform="rotate(30)"/>
        <rect x="-38" y="-38" width="76" height="76" transform="rotate(45)"/>
        <rect x="-38" y="-38" width="76" height="76" transform="rotate(60)"/>
        <rect x="-38" y="-38" width="76" height="76" transform="rotate(75)"/>
      </g>
      <circle r="40" fill="var(--ivory)" stroke="var(--badge-ring)" stroke-width="2.5"/>
      <text class="badge-text badge-text--halal" y="-3">100%</text>
      <text class="badge-text badge-text--halal" y="19">halal</text>
    </g>

    <!-- keep frozen badge -->
    <g class="badge badge--frozen" transform="translate(159 540)">
      <g fill="var(--badge-yellow)">
        <rect x="-28" y="-28" width="56" height="56"/>
        <rect x="-28" y="-28" width="56" height="56" transform="rotate(15)"/>
        <rect x="-28" y="-28" width="56" height="56" transform="rotate(30)"/>
        <rect x="-28" y="-28" width="56" height="56" transform="rotate(45)"/>
        <rect x="-28" y="-28" width="56" height="56" transform="rotate(60)"/>
        <rect x="-28" y="-28" width="56" height="56" transform="rotate(75)"/>
      </g>
      <circle r="30" fill="var(--ivory)" stroke="var(--badge-ring)" stroke-width="2"/>
      <text class="badge-text badge-text--frozen" y="-3">Keep</text>
      <text class="badge-text badge-text--frozen" y="13">Frozen</text>
    </g>
  </svg>
</main>
</body>
</html>
```